indépendant en tant que Massothérapeute et Préparateur Mental, j'ai besoin de ...

Massothérapeute et préparateur mental indépendant, je recherche une carte de visite sobre et dynamique, sans images liées au massage ou à la préparation mentale mais intégrant mon logo. Les couleurs que j'aime bien sont : Blanc, gris, anthracite, noir et jaune

carte de préférence Horizontale
neutre qui puisse toucher le deux domaines Massothérapie et préparation mentale

Requirements
Must have
• mon projet doit intégrer au recto:
LOGO
Loïc Bardemaz
078 315 26 48
info@loicbardemaz-exemple.ch
et éventuellement www.loicbardemaz-exemple.ch

et au verso les deux adresses:

Chemin des Grèvelins 7B
1400 Yverdon-les-Bains

Avenue des Mélèzes 9
1700 Fribourg

Should not have
• mon projet ne doit pas contenir d'image en liens avec le massage ni la préparation mentale.

```html
<!DOCTYPE html>
<html lang="fr">
<head>
<meta charset="utf-8">
<title>Loïc Bardemaz – Carte de visite</title>
<link rel="stylesheet" href="https://fonts.googleapis.com/css2?family=Montserrat:wght@300;400;700;800&family=Open+Sans:wght@400;600&display=swap">
<style>
  :root {
    --bg: #2a2b2d;
    --paper: #ffffff;
    --ink: #111111;
    --text: #3a3a3a;
    --yellow: #f2e600;
    --anthracite: #1f1f20;
    --pattern: #2b2b2c;
    --grey: #a9a9a9;
  }
  * { margin: 0; padding: 0; box-sizing: border-box; }
  html, body { width: 1200px; height: 898px; overflow: hidden; }
  body {
    background: var(--bg);
    position: relative;
    font-family: "Open Sans", sans-serif;
  }
  .card {
    position: absolute;
    top: 284px;
    width: 510px;
    height: 330px;
    border-radius: 22px;
    overflow: hidden;
    box-shadow: 0 18px 40px rgba(0,0,0,.45);
  }
  /* Front */
  .card--front { left: 60px; background: var(--paper); color: var(--text); }
  .front__brand {
    position: absolute; left: 36px; top: 38px;
    display: flex; align-items: center; gap: 14px;
  }
  .brand__mark { width: 18px; height: 18px; background: var(--yellow); }
  .brand__name {
    font-family: "Montserrat", sans-serif; font-weight: 800;
    font-size: 34px; color: var(--ink); letter-spacing: .5px;
  }
  .front__title {
    position: absolute; left: 36px; top: 92px;
    font-family: "Montserrat", sans-serif; font-weight: 700;
    font-size: 15px; letter-spacing: .6px; color: var(--ink);
  }
  .front__rule {
    position: absolute; left: 36px; right: 36px; top: 138px;
    height: 2px; background: var(--yellow);
  }
  .front__contacts {
    position: absolute; left: 36px; top: 168px;
    list-style: none; font-size: 14px; line-height: 26px;
  }
  .front__contacts li { display: flex; align-items: center; gap: 10px; }
  .contact__dot { width: 8px; height: 8px; border-radius: 50%; background: var(--yellow); flex: none; }
  .front__addresses {
    position: absolute; right: 36px; bottom: 34px;
    text-align: right; font-size: 14px; line-height: 20px;
  }
  .address + .address { margin-top: 14px; }
  /* Back */
  .card--back { left: 630px; background: var(--anthracite); }
  .back__pattern {
    position: absolute; inset: 0;
    background: linear-gradient(135deg, var(--pattern) 0%, var(--anthracite) 60%, #181818 100%);
  }
  .back__brand {
    position: absolute; left: 0; right: 0; top: 128px;
    display: flex; flex-direction: column; align-items: center; gap: 10px;
  }
  .back__name-row { display: flex; align-items: center; gap: 14px; }
  .back__name {
    font-family: "Montserrat", sans-serif; font-weight: 800;
    font-size: 36px; color: var(--yellow); letter-spacing: .5px;
  }
  .back__title {
    font-family: "Montserrat", sans-serif; font-weight: 400;
    font-size: 11px; letter-spacing: 1.2px; color: var(--grey);
  }
</style>
</head>
<body>
  <section class="card card--front" aria-label="Recto">
    <div class="front__brand">
      <span class="brand__mark"></span>
      <span class="brand__name">Loïc Bardemaz</span>
    </div>
    <p class="front__title">MASSOTHÉRAPEUTE / PRÉPARATEUR MENTAL</p>
    <div class="front__rule"></div>
    <ul class="front__contacts">
      <li><span class="contact__dot"></span>078 315 26 48</li>
      <li><span class="contact__dot"></span>info@loicbardemaz-exemple.ch</li>
      <li><span class="contact__dot"></span>www.loicbardemaz-exemple.ch</li>
    </ul>
    <div class="front__addresses">
      <p class="address">Chemin des Grèvelins 7B<br>1400 Yverdon-les-Bains</p>
      <p class="address">Avenue des Mélèzes 9<br>1700 Fribourg</p>
    </div>
  </section>

  <section class="card card--back" aria-label="Verso">
    <div class="back__pattern" role="img" aria-label="Motif décoratif ton sur ton anthracite en fond de carte"></div>
    <div class="back__brand">
      <div class="back__name-row">
        <span class="brand__mark"></span>
        <span class="back__name">Loïc Bardemaz</span>
      </div>
      <p class="back__title">MASSOTHÉRAPEUTE / PRÉPARATEUR MENTAL</p>
    </div>
  </section>
</body>
</html>
```